https://velormark.com

We need a cool technology design for our Managed IT Services company. We are located in Coral Springs Florida. We provide all IT services and support for small to medium sized businesses. We would like to see designs that use our blue and white colors from our website.

```html
<!DOCTYPE html>
<html lang="en">
<head>
<meta charset="utf-8">
<title>Velormark Business Card</title>
<link href="https://fonts.googleapis.com/css2?family=Montserrat:wght@700&family=Open+Sans:wght@400;600;700&display=swap" rel="stylesheet">
<style>
  :root {
    --navy: #0f2f57;
    --navy-deep: #0a2546;
    --ink: #3b3f45;
    --muted: #9a9ea4;
    --paper: #f7f7f6;
    --stage: #3a3b3d;
    --white: #ffffff;
    --url-tint: #c9d3df;
    --dot: #b9c0c8;
  }
  * { margin: 0; padding: 0; box-sizing: border-box; }
  html, body { width: 1200px; height: 960px; overflow: hidden; }
  body {
    background: var(--stage);
    display: flex;
    flex-direction: column;
    align-items: center;
    justify-content: center;
    gap: 40px;
    font-family: "Open Sans", Arial, sans-serif;
  }
  .card {
    width: 760px;
    height: 434px;
    position: relative;
    box-shadow: 0 10px 30px rgba(0,0,0,.35);
  }
  .card-back {
    background: linear-gradient(135deg, var(--navy) 0%, var(--navy-deep) 100%);
  }
  .back-name {
    position: absolute;
    left: 0; right: 0;
    top: 150px;
    text-align: center;
    font-weight: 700;
    font-size: 54px;
    letter-spacing: 1px;
    color: var(--white);
  }
  .back-url {
    position: absolute;
    left: 0; right: 0;
    top: 268px;
    text-align: center;
    font-size: 17px;
    letter-spacing: 7px;
    color: var(--url-tint);
  }
  .card-front { background: var(--paper); }
  .brand {
    position: absolute;
    top: 90px;
    right: 60px;
    display: flex;
    align-items: center;
    gap: 12px;
  }
  .brand-dot {
    width: 22px; height: 22px;
    border-radius: 50%;
    background: var(--dot);
  }
  .brand-name {
    font-weight: 700;
    font-size: 44px;
    color: var(--navy);
  }
  .contact {
    position: absolute;
    left: 64px;
    top: 140px;
  }
  .person-name {
    font-family: "Montserrat", Arial, sans-serif;
    font-weight: 700;
    font-size: 22px;
    letter-spacing: 1px;
    color: var(--navy);
  }
  .person-title {
    font-family: "Montserrat", Arial, sans-serif;
    font-weight: 700;
    font-size: 15px;
    letter-spacing: 1px;
    color: var(--muted);
    margin-bottom: 18px;
  }
  .address, .contact-line {
    font-size: 17px;
    line-height: 26px;
    color: var(--ink);
  }
  .address { margin-bottom: 4px; }
  .contact-line { display: flex; align-items: center; gap: 10px; margin-left: -24px; }
  .contact-line svg { width: 14px; height: 14px; fill: var(--navy); flex: none; }
</style>
</head>
<body>
  <section class="card card-back">
    <div class="back-name">VELORMARK</div>
    <div class="back-url">www.velormark.com</div>
  </section>

  <section class="card card-front">
    <div class="brand">
      <span class="brand-dot"></span>
      <span class="brand-name">VELORMARK</span>
    </div>
    <div class="contact">
      <div class="person-name">DANA WHITLOCK</div>
      <div class="person-title">PRESIDENT</div>
      <div class="address">2180 Harbor Pointe Blvd #410<br>Alder Bay, Oregon 97412</div>
      <div class="contact-line">
        <svg viewBox="0 0 16 16" aria-hidden="true"><path d="M3.5 1l2.5 3-1.5 2c1 2 3 4 5 5l2-1.5 3 2.5-1.5 2.5C7 15 1 9 1 2.5z"/></svg>
        <span>(555) 214-0786</span>
      </div>
      <div class="contact-line">
        <svg viewBox="0 0 16 16" aria-hidden="true"><path d="M1 3h14v10H1z M1 3l7 6 7-6" stroke="#f7f7f6" stroke-width="1.2"/></svg>
        <span>dana@velormark.com</span>
      </div>
      <div class="contact-line">
        <svg viewBox="0 0 16 16" aria-hidden="true"><circle cx="8" cy="8" r="7"/><path d="M1 8h14M8 1c3 3 3 11 0 14M8 1c-3 3-3 11 0 14" stroke="#f7f7f6" stroke-width="1" fill="none"/></svg>
        <span>www.velormark.com</span>
      </div>
    </div>
  </section>
</body>
</html>
```